Web design for community centre - bright colours (provided) and matching existing logo

Website based on a provided logo and existing website template skeleton (it is a Wordpress theme we must use that is already installed)

Basically, see if you can improve the existing theme skeleton at https://tarvolnh.org.au/redesign/. Mostly we are looking for a much nicer menu that works with the logo, and a nice font/design for text content.

We have a developer who will work your design into the Wordpress theme – so you can get creative in a graphic software app and our developer can most likely implement your ideas.

The website ideally will include design ideas from the logo (e.g. the idea of people with their arms around each other, colours).

Improvement to the text displayed on the photo slider (e.g. a colour border or other decoration) is also needed.

It needs a 'community' feel.

Target Market(s)

Parents (provides childcare), older people, people with disabilities, recent migrants

Industry/Entity Type

Community Center

Number of Pages Required

1 page

Font styles to use
Sans Serif

Colors

Designer to choose colors to be used in the design.

Requirements
Must have
• A very aesthetic top menu. Nice use of spacing, negative space etc.
• Fonts need to be legally available without a pageview fee (one off purchase OK). You need to provide proof we can use the font legally.
• See https://www.pelmoray.org.au/ for an example of a menu we like.
• Must use the existing logo, provided in this brief.
• Needs to use colours from the logo but do not need to use all of them!
• Must be workable into the theme already installed at https://tarvolnh.org.au/redesign
Nice to have
• Maybe some kind of shapes attached to each menu link (top menu0
• A use of all 5 colours on the top menu, when you hover on it
Should not have
• Serif fonts

```html
<!DOCTYPE html>
<html lang="en">
<head>
<meta charset="utf-8">
<title>Tarvol Neighbourhood Learning Centre</title>
<link rel="stylesheet" href="https://fonts.googleapis.com/css2?family=Signika:wght@300;400;600&family=Arimo:wght@400&display=swap">
<style>
:root{
  --pink:#e5076c;
  --blue:#159ee3;
  --orange:#f5821f;
  --green:#72be44;
  --purple:#5b2587;
  --ink:#333333;
  --text:#444444;
  --cream:#fdf2e4;
  --footer:#2b2b2b;
  --line:#dddddd;
  --white:#ffffff;
}
*{margin:0;padding:0;box-sizing:border-box}
html,body{width:1200px;height:3074px;overflow:hidden;background:var(--white)}
body{position:relative;font-family:"Signika",sans-serif;color:var(--ink)}
a{color:inherit;text-decoration:none}
.abs{position:absolute}

/* header */
.brand{left:111px;top:24px;display:flex;align-items:center;gap:12px}
.brand-dot{width:72px;height:72px;border-radius:50%;background:var(--pink)}
.brand-name{font-family:"Signika",sans-serif;font-weight:600;font-size:22px;line-height:23px;color:var(--ink)}
.search{left:802px;top:41px;width:286px;height:43px;display:flex;border:1px solid #cfcfcf;border-radius:3px;overflow:hidden}
.search-field{flex:1;padding-left:12px;font-size:15px;color:#666;display:flex;align-items:center;letter-spacing:.3px}
.search-btn{width:47px;background:var(--pink);display:flex;align-items:center;justify-content:center}
.header-rule{left:111px;top:122px;width:977px;height:1px;background:var(--line)}
.main-nav{left:111px;top:122px;width:977px;height:69px;display:flex;justify-content:space-between;padding:0 30px 0 30px}
.main-nav a{position:relative;font-size:14px;line-height:69px;color:var(--ink);text-transform:uppercase;padding:0 12px}
.main-nav a.is-active{color:var(--pink)}
.main-nav a.is-active::after{content:"";position:absolute;left:0;right:0;bottom:0;height:4px;background:var(--pink)}

/* hero */
.hero{left:0;top:191px;width:1200px;height:710px;background:radial-gradient(circle at 50% 55%,#b58672 0%,#7a5446 35%,#3f4a5e 70%,#2b3040 100%)}
.hero-shade{left:0;top:191px;width:1200px;height:710px;background:rgba(0,0,0,.25)}
.hero-title{left:0;top:478px;width:1200px;text-align:center;color:var(--white);font-size:53px;font-weight:600;line-height:60px;text-shadow:0 2px 6px rgba(0,0,0,.4)}
.hero-sub{left:0;top:545px;width:1200px;text-align:center;color:var(--white);font-size:38px;font-weight:600;line-height:44px;text-shadow:0 2px 6px rgba(0,0,0,.4)}
.btn{display:flex;align-items:center;justify-content:center;border-radius:40px;color:var(--white);text-transform:uppercase}
.hero-btn{left:480px;top:622px;width:241px;height:60px;background:var(--pink);font-size:16px;font-weight:600}

/* section headings */
.section-title{left:0;width:1200px;text-align:center;font-size:38px;font-weight:600;color:var(--ink);text-transform:uppercase}
.section-rule{left:566px;width:68px;height:3px;background:linear-gradient(90deg,var(--pink),var(--purple))}

/* courses */
.course{top:1041px;width:186px;height:264px;border-radius:5px;overflow:hidden;color:var(--white);text-align:center}
.course-photo{height:185px}
.course-body{height:79px;padding-top:18px}
.course-name{font-size:14px;text-transform:uppercase;line-height:20px}
.course-date{font-family:"Arimo",sans-serif;font-size:13px;line-height:22px}
.arrow{top:1119px}

/* welcome */
.welcome{left:0;top:1381px;width:1200px;height:467px;background:var(--cream)}
.welcome-title{left:111px;top:1452px;font-size:38px;font-weight:600;text-transform:uppercase;color:var(--ink)}
.welcome-title span{color:var(--pink)}
.welcome-text{left:111px;top:1520px;width:503px;font-family:"Arimo",sans-serif;font-size:13.2px;line-height:28.3px;color:var(--text);text-align:justify}
.welcome-btn{left:111px;top:1719px;width:154px;height:57px;background:var(--pink);font-size:18px}
.welcome-mark{left:687px;top:1429px;width:380px;height:380px;border-radius:50%;background:var(--white);border:14px solid #f6e4cd}

/* whats on */
.event{top:2016px;width:300px;text-align:center}
.event-icon{width:122px;height:122px;border-radius:50%;margin:0 auto;display:flex;align-items:center;justify-content:center}
.event-title{margin-top:28px;font-size:16px;text-transform:uppercase;color:var(--ink)}
.event-text{margin:14px auto 0;width:262px;font-family:"Arimo",sans-serif;font-size:12.8px;line-height:27.5px;color:var(--text)}

/* donate */
.donate{left:0;top:2336px;width:1200px;height:427px;background:linear-gradient(110deg,#e5076c 0%,#b03a9a 40%,#5f6fd4 70%,#159ee3 100%)}
.donate-title{left:0;top:2438px;width:1200px;text-align:center;color:var(--white);font-size:38px;font-weight:600;text-transform:uppercase}
.donate-text{left:300px;top:2504px;width:600px;text-align:center;color:var(--white);font-size:25px;font-weight:300;line-height:40px}
.donate-btn{left:483px;top:2604px;width:234px;height:66px;border:2px solid var(--white);font-size:21px}

/* footer */
.footer{left:0;top:2763px;width:1200px;height:311px;background:var(--footer)}
.footer-brand{left:478px;top:2800px;display:flex;align-items:center;gap:12px}
.footer-brand .brand-name{color:var(--white)}
.footer-nav{left:0;top:2902px;width:1200px;display:flex;justify-content:center;gap:48px}
.footer-nav a{font-size:13px;color:var(--white);text-transform:uppercase}
.social{top:2947px;width:36px;height:36px;border:1.5px solid var(--white);border-radius:50%}
.copyright{left:0;top:3006px;width:1200px;text-align:center;color:var(--white);font-family:"Arimo",sans-serif;font-size:13px}
</style>
</head>
<body>

<header>
  <a class="abs brand" href="https://tarvolnh.org.au/redesign/">
    <span class="brand-dot"></span>
    <span class="brand-name">Tarvol<br>Neighbourhood<br>Learning Centre</span>
  </a>
  <div class="abs search">
    <div class="search-field">SEARCH</div>
    <div class="search-btn">
      <svg width="16" height="16" viewBox="0 0 16 16"><circle cx="6.5" cy="6.5" r="4.5" fill="none" stroke="#fff" stroke-width="2"/><line x1="10" y1="10" x2="14" y2="14" stroke="#fff" stroke-width="2.4" stroke-linecap="round"/></svg>
    </div>
  </div>
  <div class="abs header-rule"></div>
  <nav class="abs main-nav">
    <a class="is-active" href="#">Home</a>
    <a href="#">What's On</a>
    <a href="#">Courses</a>
    <a href="#">Freeseat Cafe</a>
    <a href="#">Programs</a>
    <a href="#">Contact</a>
    <a href="#">Tarvol Cares</a>
  </nav>
</header>

<section>
  <div class="abs hero" role="img" aria-label="Children sitting in a circle on a colourful parachute, joining hands in the centre"></div>
  <div class="abs hero-shade"></div>
  <h1 class="abs hero-title">TARVOL NEIGHBOURHOOD</h1>
  <p class="abs hero-sub">LEARNING CENTRE</p>
  <a class="abs btn hero-btn" href="#">View Course Brochure</a>
</section>

<section>
  <h2 class="abs section-title" style="top:940px">Our Courses</h2>
  <div class="abs section-rule" style="top:999px"></div>

  <svg class="abs arrow" style="left:52px" width="26" height="78" viewBox="0 0 26 78"><polyline points="24,1 2,39 24,77" fill="none" stroke="#888" stroke-width="1.2"/></svg>
  <svg class="abs arrow" style="left:1126px" width="26" height="78" viewBox="0 0 26 78"><polyline points="2,1 24,39 2,77" fill="none" stroke="#888" stroke-width="1.2"/></svg>

  <article class="abs course" style="left:111px">
    <div class="course-photo" role="img" aria-label="Person painting at a table with brushes in jars" style="background:linear-gradient(135deg,#3a2f2a,#8a7a6e)"></div>
    <div class="course-body" style="background:var(--pink)"><div class="course-name">Barista Training</div><div class="course-date">Monday 16th September</div></div>
  </article>
  <article class="abs course" style="left:309px">
    <div class="course-photo" role="img" aria-label="Toddler playing on a floor mat" style="background:linear-gradient(135deg,#b59a86,#6e5c52)"></div>
    <div class="course-body" style="background:var(--blue)"><div class="course-name">The Young at Heart</div><div class="course-date">Monday 7th October</div></div>
  </article>
  <article class="abs course" style="left:507px">
    <div class="course-photo" role="img" aria-label="Entrance of the learning centre building" style="background:linear-gradient(135deg,#5a2a22,#2b2b2b)"></div>
    <div class="course-body" style="background:var(--orange)"><div class="course-name">Ukulele</div><div class="course-date">Monday 7th October</div></div>
  </article>
  <article class="abs course" style="left:705px">
    <div class="course-photo" role="img" aria-label="Colourful painted artwork" style="background:linear-gradient(135deg,#2f7fa0,#c6683f,#4a6a3a)"></div>
    <div class="course-body" style="background:var(--green)"><div class="course-name">Tai Chi Arthritis</div><div class="course-date">Monday 7th October</div></div>
  </article>
  <article class="abs course" style="left:903px">
    <div class="course-photo" role="img" aria-label="Students working at computers in a classroom" style="background:linear-gradient(135deg,#d9d9d9,#7a6f6a)"></div>
    <div class="course-body" style="background:var(--purple)"><div class="course-name">EAL</div><div class="course-date">Monday 7th October</div></div>
  </article>
</section>

<section>
  <div class="abs welcome"></div>
  <h2 class="abs welcome-title">Welcome to <span>TNLC</span></h2>
  <p class="abs welcome-text">Freeseat is a social enterprise cafe leading the way in sustainable food production, use and paying it forward. 100% of our profits help vulnerable learners in our community to participate in education and skill building activities. Pay us a visit – taste the amazing coffee and try our ‘kitchen garden to table’ plates, your coffee or meal is helping someone achieve their goals.&nbsp; Or pay a coffee or meal forward to someone who might be down on their luck. We look forward to serving you</p>
  <a class="abs btn welcome-btn" href="#">Read More</a>
  <div class="abs welcome-mark"></div>
</section>

<section>
  <h2 class="abs section-title" style="top:1896px">What's On</h2>
  <div class="abs section-rule" style="top:1955px"></div>

  <article class="abs event" style="left:116px">
    <div class="event-icon" style="background:var(--pink)">
      <svg width="40" height="40" viewBox="0 0 40 40" fill="none" stroke="#fff" stroke-width="2.5"><rect x="3" y="7" width="34" height="30" rx="2"/><line x1="3" y1="15" x2="37" y2="15"/><line x1="11" y1="3" x2="11" y2="10"/><line x1="29" y1="3" x2="29" y2="10"/><line x1="3" y1="22" x2="37" y2="22" stroke-width="1.5"/><line x1="3" y1="29" x2="37" y2="29" stroke-width="1.5"/><line x1="12" y1="15" x2="12" y2="37" stroke-width="1.5"/><line x1="20" y1="15" x2="20" y2="37" stroke-width="1.5"/><line x1="28" y1="15" x2="28" y2="37" stroke-width="1.5"/></svg>
    </div>
    <h3 class="event-title">Yarra River Cruise Excursion</h3>
    <p class="event-text">Join us for a relaxing cruise along the Yarra River 9.30am Depart TNLC and travel by tram to the Townhall and make</p>
  </article>
  <article class="abs event" style="left:448px">
    <div class="event-icon" style="background:var(--blue)">
      <svg width="38" height="38" viewBox="0 0 38 38"><circle cx="19" cy="19" r="18" fill="#fff"/><circle cx="19" cy="10.5" r="3" fill="#159ee3"/><path d="M15 16h6v11h2.5v3h-9v-3H17v-8h-2z" fill="#159ee3"/></svg>
    </div>
    <h3 class="event-title">Tarvol Cares</h3>
    <p class="event-text">It's hard to pinpoint just when Tarvol Cares began - a passing conversation at an art show, a new with a neighbouring organisation</p>
  </article>
  <article class="abs event" style="left:777px">
    <div class="event-icon" style="background:var(--green)">
      <svg width="42" height="30" viewBox="0 0 42 30"><rect x="0" y="2" width="28" height="26" rx="4" fill="#fff"/><path d="M30 11l12-8v24l-12-8z" fill="#fff"/></svg>
    </div>
    <h3 class="event-title">TNLC Short Films</h3>
    <p class="event-text">Check out our new Vidora and Streamtube channels!&nbsp; Now you can view all the amazing work that goes on at TNLC</p>
  </article>
</section>

<section>
  <div class="abs donate" role="img" aria-label="Children drawing together at a table, tinted pink to blue"></div>
  <h2 class="abs donate-title">Support us with a donation</h2>
  <p class="abs donate-text">Your donation will be directed towards the program of your choosing All donations tax deductible</p>
  <a class="abs btn donate-btn" href="#">Donate Now</a>
</section>

<footer>
  <div class="abs footer"></div>
  <a class="abs footer-brand" href="https://tarvolnh.org.au/redesign/">
    <span class="brand-dot"></span>
    <span class="brand-name">Tarvol<br>Neighbourhood<br>Learning Centre</span>
  </a>
  <nav class="abs footer-nav">
    <a href="#">Home</a>
    <a href="#">What's On</a>
    <a href="#">Courses</a>
    <a href="#">Freeseat Cafe</a>
    <a href="#">Programs</a>
    <a href="#">Contact</a>
    <a href="#">Tarvol Cares</a>
  </nav>
  <a class="abs social" style="left:496px" href="#" aria-label="Social profile 1"></a>
  <a class="abs social" style="left:539px" href="#" aria-label="Social profile 2"></a>
  <a class="abs social" style="left:582px" href="#" aria-label="Social profile 3"></a>
  <a class="abs social" style="left:625px" href="#" aria-label="Social profile 4"></a>
  <a class="abs social" style="left:668px" href="#" aria-label="Social profile 5"></a>
  <p class="abs copyright">© Copyright-2019 Tarvol nlc.All rights reserved.</p>
</footer>

</body>
</html>
```